Qorvane Management LLC Business Card

The sample logo was attached for the business Card Design for Traffic Control Company named Qorvane Management LLC. Card design needs to have the company logo and colors match the logo color. It will be nice to show some images of Traffic control signs or cones, even roads closer that math the company services

Target Market(s)

Temporary traffic control. Road closer.

Industry/Entity Type

Construction

Contact Information for Business Card

basic information, name, job title, address, email phone, website

Font styles to use
Serif
Sans Serif

Colors
F0912C
F2A743
F7CA91
FBE8D2
FDF5EE
EE7325
F08F49
F5BC92
FAE3D3
FDF4ED

```html
<!DOCTYPE html>
<html lang="en">
<head>
<meta charset="utf-8">
<title>Qorvane Management LLC – Business Card</title>
<link rel="stylesheet" href="https://fonts.googleapis.com/css2?family=Montserrat:wght@400;500;700&display=swap">
<style>
  :root {
    --page-bg: #e7e3de;
    --card-bg: #f4f2ef;
    --card-edge: #cfcac4;
    --brand-orange: #e0552b;
    --ink: #3d3d3f;
    --sign-yellow: #e8b820;
    --sign-deep: #c99612;
  }
  * { margin: 0; padding: 0; box-sizing: border-box; }
  html, body {
    width: 1200px; height: 969px; overflow: hidden;
    background: var(--page-bg);
    font-family: "Montserrat", sans-serif;
    color: var(--ink);
  }
  .business-card {
    position: absolute; left: 100px; top: 200px;
    width: 1000px; height: 570px;
    background: var(--card-bg);
    border: 1px solid var(--card-edge);
    overflow: hidden;
  }
  .company-name {
    position: absolute; left: 64px; top: 52px;
    font-weight: 700; color: var(--brand-orange);
  }
  .company-name .brand-word {
    display: block; font-size: 80px; line-height: 1; letter-spacing: 0.5px;
  }
  .company-name .brand-suffix {
    display: block; margin-top: 14px; font-size: 32px; line-height: 1; letter-spacing: 1.5px;
  }
  .accent-bar {
    position: absolute; left: 0; top: 233px;
    width: 10px; height: 58px; background: var(--brand-orange);
  }
  .person-name {
    position: absolute; left: 64px; top: 230px;
    font-weight: 700; font-size: 32px; line-height: 1.1; color: var(--ink);
  }
  .person-title {
    position: absolute; left: 64px; top: 266px;
    font-weight: 500; font-size: 22px; line-height: 1.2; color: var(--brand-orange);
  }
  .address {
    position: absolute; left: 64px; top: 303px;
    font-size: 22px; line-height: 28px; font-style: normal;
  }
  .contact-list {
    position: absolute; left: 66px; top: 371px;
    list-style: none; font-size: 22px; line-height: 28.5px;
  }
  .contact-list li { display: flex; align-items: center; gap: 12px; }
  .contact-list svg { width: 19px; height: 19px; fill: var(--brand-orange); flex: none; }
  .sign-visual {
    position: absolute; left: 529px; top: 50px;
    width: 396px; height: 520px;
    border-radius: 6px 6px 0 0;
    background: linear-gradient(180deg, var(--sign-yellow) 0%, var(--sign-deep) 70%, #8f8a80 100%);
  }
</style>
</head>
<body>
  <section class="business-card">
    <h1 class="company-name">
      <span class="brand-word">Qorvane</span>
      <span class="brand-suffix">MANAGEMENT LLC</span>
    </h1>

    <div class="accent-bar"></div>
    <h2 class="person-name">DANIEL HARLOW</h2>
    <p class="person-title">President</p>

    <address class="address">4120 Birchwood Court<br>Anchorage, Alaska 34810</address>

    <ul class="contact-list">
      <li>
        <svg viewBox="0 0 24 24"><path d="M6.6 10.8a15 15 0 0 0 6.6 6.6l2.2-2.2a1 1 0 0 1 1-.25 11.4 11.4 0 0 0 3.6.57 1 1 0 0 1 1 1V20a1 1 0 0 1-1 1A17 17 0 0 1 3 4a1 1 0 0 1 1-1h3.5a1 1 0 0 1 1 1c0 1.25.2 2.45.57 3.57a1 1 0 0 1-.25 1z"/></svg>
        369-480-2173
      </li>
      <li>
        <svg viewBox="0 0 24 24"><path d="M7 1h10a2 2 0 0 1 2 2v18a2 2 0 0 1-2 2H7a2 2 0 0 1-2-2V3a2 2 0 0 1 2-2zm0 3v15h10V4z"/></svg>
        369-604-3391
      </li>
      <li>
        <svg viewBox="0 0 24 24"><path d="M7 2h10v5H7zM4 8h16a2 2 0 0 1 2 2v8h-4v4H6v-4H2v-8a2 2 0 0 1 2-2zm4 8v4h8v-4z"/></svg>
        369-718-2046
      </li>
      <li>
        <svg viewBox="0 0 24 24"><path d="M3 5h18a1 1 0 0 1 1 1v12a1 1 0 0 1-1 1H3a1 1 0 0 1-1-1V6a1 1 0 0 1 1-1zm1 2.3V17h16V7.3l-8 5.2z"/></svg>
        name@qorvanemanagement.com
      </li>
      <li>
        <svg viewBox="0 0 24 24"><circle cx="12" cy="12" r="10"/></svg>
        www.qorvanemanagement.com
      </li>
    </ul>

    <div class="sign-visual" role="img" aria-label="Photo of a yellow diamond traffic-signal warning sign on a post"></div>
  </section>
</body>
</html>
```